15 ft high by 10 ft wide road side sign

road side sign - this is a dual carrigeway speeds of 40 mph so eye time to see ,read and absorb very short is less than 3 seconds 45,000 vehicles a day go past these are local to us our most profitable business is customers instore we embroider company and club and school logos and badges one mile ahead of this sign we have over 400,000 logos we have sewn and are on our servers we are well know in our area we can sew your logo in under 2 hours if it is already on our server we have a fast track service which we charge extra for very profitable is the customers buying items on vortiq and shopnu we can really be fast on your own items if you bring them instore we have 15 large multi head machine to cope no one else is that fast on line embroidery takes 7 -10 days we have purchased from others saying 24 hours when put to the test they fail and give excusses why it cannot be do every time we have brought and our customers say the same project your logo embrodery one mile ahead ------- road side sign 15 ft high 10 feet wide company name Swift Thread & Stitchworks 12 Harrowgate Close KT7 4PD like drivers to be able to drop off and collect sameday because driving you have very very little time to read has to be simple good thing is its a major commutor route A10 Enfield so drivers can be trained via repeat reading dale finch

Target Market(s)

our local area is our most profitable market getting people instore online is to slow to for our custopmers and low a margin for us 1,000,000 people withing 2 miles of our store

Industry/Entity Type

Embroidery

Font styles to use
Sans Serif

Colors

Designer to choose colors to be used in the design.

Requirements
Must have
• simple easy to read
• also
• nigel parsons lovers he has NP sewn on his union jack boxer shorts
• as clothing with your company logo are 100% tax deductable for most companies
• as promotional wear
Should not have
• to complicated to read and understand so many people driving past are not english readers as there main language

```html
<!DOCTYPE html>
<html lang="en">
<head>
<meta charset="utf-8">
<title>Swift Thread &amp; Stitchworks – Roadside Sign</title>
<link rel="stylesheet" href="https://fonts.googleapis.com/css2?family=Arimo:wght@700&family=Roboto+Condensed:wght@700&display=swap">
<style>
  :root {
    --sign-red: #c93c33;
    --sign-blue: #44558a;
    --sign-white: #ffffff;
    --backdrop: #e4e6ea;
  }
  * { box-sizing: border-box; margin: 0; padding: 0; }
  html, body {
    width: 1200px;
    height: 675px;
    overflow: hidden;
  }
  body {
    background: var(--backdrop);
    display: flex;
    align-items: center;
    justify-content: center;
  }
  .roadside-sign {
    width: 400px;
    height: 600px;
    display: flex;
    flex-direction: column;
    background: var(--sign-white);
  }
  .edge-stripe {
    height: 12px;
    flex: none;
    background: var(--sign-red);
  }
  .company-band {
    height: 124px;
    display: flex;
    flex-direction: column;
    align-items: center;
    justify-content: center;
    font-family: "Arimo", Arial, sans-serif;
    font-weight: 700;
    font-size: 34px;
    line-height: 1.08;
    color: var(--sign-red);
    text-transform: uppercase;
    text-align: center;
  }
  .service-band {
    height: 172px;
    background: var(--sign-blue);
    display: flex;
    flex-direction: column;
    align-items: center;
    justify-content: center;
    font-family: "Roboto Condensed", "Arial Narrow", sans-serif;
    font-weight: 700;
    font-size: 56px;
    line-height: 1;
    color: var(--sign-white);
    text-transform: uppercase;
    text-align: center;
  }
  .speed-band {
    height: 70px;
    background: var(--sign-red);
    display: flex;
    align-items: center;
    justify-content: center;
    font-family: "Roboto Condensed", "Arial Narrow", sans-serif;
    font-weight: 700;
    font-size: 38px;
    color: var(--sign-white);
    text-transform: uppercase;
  }
  .distance-band {
    height: 90px;
    display: flex;
    align-items: center;
    justify-content: center;
    gap: 12px;
    font-family: "Roboto Condensed", "Arial Narrow", sans-serif;
    font-weight: 700;
    font-size: 42px;
    color: var(--sign-blue);
    text-transform: uppercase;
    border-bottom: 4px solid var(--sign-blue);
  }
  .ahead-arrow {
    width: 38px;
    height: 44px;
    fill: var(--sign-blue);
  }
  .address-band {
    height: 120px;
    display: flex;
    flex-direction: column;
    align-items: center;
    justify-content: center;
    font-family: "Roboto Condensed", "Arial Narrow", sans-serif;
    font-weight: 700;
    font-size: 34px;
    line-height: 1.15;
    color: var(--sign-red);
    text-align: center;
    white-space: nowrap;
  }
</style>
</head>
<body>
  <main class="roadside-sign">
    <div class="edge-stripe"></div>
    <h1 class="company-band">
      <span class="company-line">Swift Thread</span>
      <span class="company-line">&amp; Stitchworks</span>
    </h1>
    <p class="service-band">
      <span class="service-line">Logo Embroid</span>
      <span class="service-line">and Print</span>
    </p>
    <p class="speed-band">Same Day Service</p>
    <p class="distance-band">
      <svg class="ahead-arrow" viewBox="0 0 38 44" aria-hidden="true">
        <polygon points="19,0 38,20 26,20 26,44 12,44 12,20 0,20"/>
      </svg>
      <span>One Mile Ahead</span>
    </p>
    <p class="address-band">
      <span class="address-line">12 Harrowgate Close,</span>
      <span class="address-line">KT7 4PD</span>
    </p>
    <div class="edge-stripe"></div>
  </main>
</body>
</html>
```